Takeout menu

I need a takeout menu for Casa Lumo in Westerly RI. It needs just the location, phone number, items and descriptions from my square site- no pricing listed. No hours listed as I am seasonal and they change during the year. Must say "please inform us of any food allergies prior to ordering" somewhere on it, per order of health dept. I will most likely be printing in b/w.

```html
<!DOCTYPE html>
<html lang="en">
<head>
<meta charset="utf-8">
<title>Casa Lumo – Takeout Menu</title>
<link rel="stylesheet" href="https://fonts.googleapis.com/css2?family=Alegreya:ital,wght@0,400;0,700;0,800;0,900;1,400&family=Poppins:wght@400;500&display=swap">
<style>
:root{
  --ink:#0b0b0b;
  --paper:#ffffff;
  --backdrop:#e6e6e6;
  --rule:#c9c9c9;
  --serif:"Alegreya", Georgia, serif;
  --sans:"Poppins", Arial, sans-serif;
}
*{box-sizing:border-box;margin:0;padding:0}
html,body{width:1200px;height:826px;overflow:hidden;background:var(--backdrop)}
.canvas{position:relative;width:1200px;height:826px}
.page{position:absolute;top:76px;width:481px;height:674px;background:var(--paper);color:var(--ink);font-family:var(--serif)}
.page--front{left:86px}
.page--back{left:632px}
.frame{position:absolute;left:16px;right:16px;top:13px;height:608px;border:1px dashed var(--ink);border-bottom:none}
.brand{position:absolute;display:flex;align-items:center;gap:5px;font-family:var(--serif);font-weight:800;font-size:14px;color:var(--ink);left:0;right:0;justify-content:center}
.brand__dot{width:10px;height:10px;border-radius:50%;background:var(--ink)}
.welcome{position:absolute;top:98px;left:0;right:0;text-align:center;font-size:25px;font-weight:400;letter-spacing:.5px}
.title{position:absolute;top:120px;left:0;right:0;text-align:center;font-size:64px;font-weight:900;line-height:1;letter-spacing:-.5px}
.ribbon{position:absolute;height:22px}
.ribbon svg{position:absolute;inset:0;width:100%;height:100%}
.ribbon span{position:relative;display:block;text-align:center;line-height:22px;color:var(--paper);font-weight:900;font-size:16px;letter-spacing:.6px}
.note{position:absolute;left:0;right:0;text-align:center;font-style:italic;font-size:12px;color:var(--ink)}
.note--small{font-size:9px}
.intro{position:absolute;left:0;right:0;text-align:center;font-family:var(--sans);font-size:8px;line-height:10px}
.divider{position:absolute;left:240px;width:1px;background:var(--rule)}
.item{position:absolute;width:160px}
.item--wide{width:175px}
.item h3{font-weight:800;font-size:10.5px;line-height:12px}
.item p{font-style:italic;font-size:5.4px;line-height:6.8px;margin-top:1px}
.allergy{position:absolute;top:599px;left:0;right:0;text-align:center;font-family:var(--sans);font-weight:500;font-size:9px}
.contact{position:absolute;top:621px;left:0;right:0;height:27px;background:var(--ink);display:flex;align-items:center;justify-content:center;gap:14px;color:var(--paper);font-size:11px;letter-spacing:.3px}
.contact__item{display:flex;align-items:center;gap:4px;white-space:nowrap}
.contact__item svg{width:17px;height:17px}
</style>
</head>
<body>
<div class="canvas">

  <section class="page page--front">
    <div class="frame"></div>
    <div class="brand" style="top:52px"><i class="brand__dot"></i>Casa Lumo</div>
    <div class="welcome">WELCOME TO</div>
    <h1 class="title">Casa Lumo</h1>

    <div class="ribbon" style="left:124px;width:228px;top:195px">
      <svg viewBox="0 0 228 22" preserveAspectRatio="none"><polygon points="0,0 228,0 214,11 228,22 0,22 14,11" fill="#0b0b0b"/></svg>
      <span>RED PIZZAS</span>
    </div>
    <div class="note" style="top:222px">all pizzas are 14"</div>

    <div class="divider" style="top:252px;height:325px"></div>

    <div class="item" style="left:61px;top:254px"><h3>Mozzarella</h3><p>Crushed tomato sauce, shredded whole milk mozzarella, grated parmesan and pecorino cheeses, garlic infused extra virgin olive oil</p></div>
    <div class="item" style="left:61px;top:300px"><h3>The Vinci</h3><p>shredded whole milk mozzarella, fresh mozzarella, fresh basil sauce on top, grated parmesan and pecorino, garlic oil. This is similar to a NY-style margherita pizza</p></div>
    <div class="item" style="left:61px;top:351px"><h3>Toscano</h3><p>Bar-style (flat and crispy) pizza with whole-milk mozzarella pecorino, parmesan, crushed tomato sauce on top, garlic-infused extra virgin oil, and seasoned with oregano and crushed red chili flakes.</p></div>
    <div class="item" style="left:61px;top:406px"><h3>Meatball Combo</h3><p>mozzarella pie base, slices of house-made meatballs roasted peppers, and sautéed onions</p></div>
    <div class="item" style="left:61px;top:456px"><h3>West Coast Combo</h3><p>Mozzarella pie with sliced local sausage, roasted mushrooms, and black olives</p></div>
    <div class="item" style="left:61px;top:503px"><h3>Pepperoni Supreme</h3><p>mozzarella pie base with roasted mushrooms, and vinegar peppers</p></div>
    <div class="item" style="left:61px;top:554px"><h3>Gar-Leek</h3><p>mozzarella pie base, garlic confit, buttery leeks</p></div>

    <div class="item item--wide" style="left:284px;top:254px"><h3>Pepperoni</h3><p>mozzarella pie base, pepperoni cups</p></div>
    <div class="item item--wide" style="left:284px;top:300px"><h3>Margherita</h3><p>crushed tomato sauce, fresh mozzarella, fresh basil, parmesan pecorino, garlic oil</p></div>
    <div class="item item--wide" style="left:284px;top:351px"><h3>Sausage Combo</h3><p>mozzarella pie base, cup &amp; char sausage, roasted peppers sautéed onions</p></div>
    <div class="item item--wide" style="left:284px;top:406px"><h3>Soupy Combo</h3><p>mozzarella pie base, local soppressata, roasted peppers sautéed onions</p></div>
    <div class="item item--wide" style="left:284px;top:456px"><h3>El Jefe</h3><p>Mozzarella pizza with cup and char sausage, roasted onions, and banana peppers.</p></div>
    <div class="item item--wide" style="left:284px;top:503px"><h3>Hawaiian</h3><p>pepperoni pie base, roasted green hatch chiles (medium spice level), fresh cut pineapple</p></div>
    <div class="item item--wide" style="left:284px;top:547px"><h3>Towner</h3><p>Start with a Toscano pie, then add roasted tomatoes buttery leeks, and house-made meatball.</p></div>

    <p class="allergy">Please Inform Us Of Any Food Allergies Prior To Ordering</p>

    <footer class="contact">
      <span class="contact__item"><svg viewBox="0 0 20 20"><circle cx="10" cy="10" r="10" fill="#fff"/><path d="M6.2 4.6l2 2.2-1 1.6c.8 1.7 2 2.9 3.7 3.7l1.6-1 2.2 2-1.2 2c-4.4-.3-8-3.9-8.3-8.3z" fill="#0b0b0b"/></svg>401-555-0142</span>
      <span class="contact__item"><svg viewBox="0 0 20 20"><circle cx="10" cy="10" r="10" fill="#fff"/><path d="M10 3.6a4.4 4.4 0 0 0-4.4 4.4c0 3.3 4.4 8.4 4.4 8.4s4.4-5.1 4.4-8.4A4.4 4.4 0 0 0 10 3.6z" fill="#0b0b0b"/><circle cx="10" cy="8" r="1.7" fill="#fff"/></svg>12 Harbor Ln Lumo Bay, RI 02800</span>
      <span class="contact__item"><svg viewBox="0 0 20 20"><circle cx="10" cy="10" r="10" fill="#fff"/><g fill="none" stroke="#0b0b0b" stroke-width="1"><circle cx="10" cy="10" r="5.5"/><ellipse cx="10" cy="10" rx="2.4" ry="5.5"/><path d="M4.5 10h11M5.3 7.3h9.4M5.3 12.7h9.4"/></g></svg>www.casalumori.com</span>
    </footer>
  </section>

  <section class="page page--back">
    <div class="frame"></div>
    <div class="brand" style="top:38px"><i class="brand__dot"></i>Casa Lumo</div>

    <div class="ribbon" style="left:148px;width:182px;top:75px">
      <svg viewBox="0 0 182 22" preserveAspectRatio="none"><polygon points="0,0 182,0 168,11 182,22 0,22 14,11" fill="#0b0b0b"/></svg>
      <span>WHITE PIZZAS</span>
    </div>
    <div class="note note--small" style="top:101px">all pizzas are 14"</div>

    <div class="divider" style="top:120px;height:132px"></div>
    <div class="item" style="left:60px;top:118px"><h3>White</h3><p>shredded mozzarella, fresh mozzarella, pecorino, parmesan ricotta, fresh basil, garlic oil (no sauce)</p></div>
    <div class="item" style="left:60px;top:157px"><h3>Spinach B.L.T.</h3><p>spinach pie base, buttery leeks, bacon, roasted tomatoes</p></div>
    <div class="item" style="left:60px;top:187px"><h3>Potato Pie</h3><p>sliced russets, buttery leeks, fresh mozzarella, medium cheddar bacon, parmesan, pecorino, garlic oil (no sauce)</p></div>
    <div class="item" style="left:60px;top:226px"><h3>Spinach</h3><p>white pie base, baby spinach, garlic confit</p></div>
    <div class="item item--wide" style="left:271px;top:118px"><h3>Apple Pie</h3><p>medium cheddar, parmesan, pecorino, tart apples, bacon fresh mozzarella, sautéed onions, garlic oil, and comes with a side of hot honey to drizzle</p></div>
    <div class="item item--wide" style="left:271px;top:171px"><h3>Veggie</h3><p>white pie base with fresh spinach, roasted mushrooms, roasted peppers, sautéed onions, roasted tomatoes</p></div>
    <div class="item item--wide" style="left:271px;top:219px"><h3>Chicken Bacon Ranch</h3><p>shredded mozzarella, cheddar, roasted chicken, bacon, leeks roasted tomatoes, ranch drizzle</p></div>

    <div class="ribbon" style="left:146px;width:189px;top:272px">
      <svg viewBox="0 0 189 22" preserveAspectRatio="none"><polygon points="0,0 189,0 175,11 189,22 0,22 14,11" fill="#0b0b0b"/></svg>
      <span>CUSTOM PIZZA</span>
    </div>
    <p class="intro" style="top:298px">Start with either our red or white pie and add what you'd like!<br>Build your own whole pie or half/half!</p>

    <div class="divider" style="top:329px;height:32px"></div>
    <div class="item" style="left:60px;top:329px"><h3>BYOP Mozzarella</h3><p>starts with crushed tomato sauce, shredded mozzarella parmesan, pecorino, garlic oil</p></div>
    <div class="item item--wide" style="left:271px;top:329px"><h3>BYOP White</h3><p>starts with shredded mozzarella, fresh mozzarella, pecorino, parmesan ricotta, fresh basil, garlic oil (no sauce)</p></div>

    <div class="ribbon" style="left:177px;width:127px;top:376px">
      <svg viewBox="0 0 127 22" preserveAspectRatio="none"><polygon points="0,0 127,0 113,11 127,22 0,22 14,11" fill="#0b0b0b"/></svg>
      <span>GREENS</span>
    </div>
    <div class="divider" style="top:406px;height:32px"></div>
    <div class="item" style="left:60px;top:406px"><h3>Caesar Salad</h3><p>With house-made sourdough croutons, shaved parmesan lemon wedge, and 2 house-made Caesar dressings</p></div>
    <div class="item item--wide" style="left:271px;top:406px"><h3>Chop Salad</h3><p>Mixed greens, diced chicken, bacon, gorgonzola, ditalini pasta, red onion roasted tomatoes, with 2 sides of house-made balsamic vinaigrette.</p></div>

    <div class="ribbon" style="left:193px;width:95px;top:456px">
      <svg viewBox="0 0 95 22" preserveAspectRatio="none"><polygon points="0,0 95,0 81,11 95,22 0,22 14,11" fill="#0b0b0b"/></svg>
      <span>SIDES</span>
    </div>
    <div class="divider" style="top:488px;height:97px"></div>
    <div class="item" style="left:60px;top:488px"><h3>Fries</h3><p>house-cut!</p></div>
    <div class="item" style="left:60px;top:517px"><h3>Garlic Focaccia Bread</h3><p>A lightly stretched dough, shredded whole milk mozzarella, pecorino and parmesan cheeses, and lots of garlic infused extra virgin olive oil. comes with a side of house-made marinara</p></div>
    <div class="item" style="left:60px;top:560px"><h3>Fuentes Soda</h3><p>Choose a flavor</p></div>
    <div class="item item--wide" style="left:271px;top:488px"><h3>Wings</h3><p>6 crispy wingdings tossed in your choice of sauce, or plain</p></div>
    <div class="item item--wide" style="left:271px;top:525px"><h3>Chicken Nuggets</h3><p>For the kids! 10 piece</p></div>
    <div class="item item--wide" style="left:271px;top:560px"><h3>Soda</h3><p>12oz can. Choose a flavor</p></div>

    <p class="allergy">Please Inform Us Of Any Food Allergies Prior To Ordering</p>

    <footer class="contact">
      <span class="contact__item"><svg viewBox="0 0 20 20"><circle cx="10" cy="10" r="10" fill="#fff"/><path d="M6.2 4.6l2 2.2-1 1.6c.8 1.7 2 2.9 3.7 3.7l1.6-1 2.2 2-1.2 2c-4.4-.3-8-3.9-8.3-8.3z" fill="#0b0b0b"/></svg>401-555-0142</span>
      <span class="contact__item"><svg viewBox="0 0 20 20"><circle cx="10" cy="10" r="10" fill="#fff"/><path d="M10 3.6a4.4 4.4 0 0 0-4.4 4.4c0 3.3 4.4 8.4 4.4 8.4s4.4-5.1 4.4-8.4A4.4 4.4 0 0 0 10 3.6z" fill="#0b0b0b"/><circle cx="10" cy="8" r="1.7" fill="#fff"/></svg>12 Harbor Ln Lumo Bay, RI 02800</span>
      <span class="contact__item"><svg viewBox="0 0 20 20"><circle cx="10" cy="10" r="10" fill="#fff"/><g fill="none" stroke="#0b0b0b" stroke-width="1"><circle cx="10" cy="10" r="5.5"/><ellipse cx="10" cy="10" rx="2.4" ry="5.5"/><path d="M4.5 10h11M5.3 7.3h9.4M5.3 12.7h9.4"/></g></svg>www.casalumori.com</span>
    </footer>
  </section>

</div>
</body>
</html>
```